Business Card and Stationary Design

After the successful redesign of our logo we are wanting to follow suite and create a new business card and stationary design!

New Logo is attached, information required on the business card should contain a mixture of the following but layout/arrangement is up to the designer.

Happy if the national provider number and abn are on the back, and happy for them to be smaller than the rest.

I am also happy to receive single sided or weird and wonderful designs.

Name
Title
National Provider Number 7192
ABN 53 614 289 117
Level 1, 214 Garrow Street
Kelbridge NSW 2291
Ph: 1300 587 902
Mobile: 0438 761 205
name@ironquillbuild.com.au
www.ironquillbuild.com.au

Target Market(s)

Professionals, Peers, Students, Suppliers...

Industry/Entity Type

Construction

Contact Information for Business Card

Listed in project description

Font styles to use
Other font styles liked:
• Century Gothic

Colors
0455a3
3176b5
ffffff

Requirements
Must have
• Professional Design, same color scheme as our logo
Nice to have
• Something that sets our apart from everyone else would be fantastic, open to size and shape and layout options, as long as they present professionally.
• Open to raised/embossed text, alternative materials, custom sizes, clear material
Should not have
• The color orange

```html
<!DOCTYPE html>
<html lang="en">
<head>
<meta charset="utf-8">
<title>Ironquill Build – Business Card</title>
<link rel="stylesheet" href="https://fonts.googleapis.com/css2?family=Questrial&family=Mulish:wght@700&display=swap">
<style>
  :root {
    --backdrop: #3a3a3a;
    --navy: #0b3b7c;
    --navy-deep: #07336c;
    --navy-text: #123e7b;
    --grey-text: #8a8a8a;
    --paper: #ffffff;
  }
  * { box-sizing: border-box; margin: 0; padding: 0; }
  html, body { width: 1200px; height: 900px; overflow: hidden; }
  body {
    background: var(--backdrop);
    font-family: "Questrial", "Century Gothic", sans-serif;
    position: relative;
  }
  .card {
    position: absolute;
    top: 302px;
    width: 513px;
    height: 295px;
  }
  .card--back {
    left: 73px;
    background: var(--navy);
  }
  .card--back .texture {
    position: absolute;
    inset: 0;
    background: linear-gradient(135deg, var(--navy) 0%, var(--navy-deep) 55%, var(--navy) 100%);
  }
  .brand {
    display: flex;
    align-items: center;
    gap: 10px;
    white-space: nowrap;
  }
  .brand__square { flex: none; }
  .brand__name { line-height: 1; }
  .card--back .brand {
    position: absolute;
    left: 86px;
    top: 118px;
  }
  .card--back .brand__square { width: 58px; height: 58px; background: var(--paper); }
  .card--back .brand__name { color: var(--paper); font-size: 38px; }

  .card--front {
    left: 615px;
    background: var(--paper);
  }
  .card--front .brand {
    position: absolute;
    right: 33px;
    top: 36px;
  }
  .card--front .brand__square { width: 44px; height: 44px; background: var(--navy); }
  .card--front .brand__name { color: var(--navy-text); font-size: 28px; }

  .person {
    position: absolute;
    left: 40px;
    top: 130px;
  }
  .person__name {
    font-family: "Mulish", "Century Gothic", sans-serif;
    font-weight: 700;
    font-size: 15px;
    line-height: 18px;
    color: var(--navy-text);
  }
  .person__title {
    font-size: 13px;
    line-height: 16px;
    color: var(--grey-text);
    letter-spacing: 0.3px;
  }
  .contacts {
    position: absolute;
    left: 40px;
    top: 176px;
    list-style: none;
    font-size: 13.5px;
    line-height: 16.5px;
    color: var(--navy-text);
  }
  .contacts__label {
    display: inline-block;
    width: 18px;
    color: var(--grey-text);
  }
  .registration {
    position: absolute;
    right: 33px;
    top: 219px;
    text-align: right;
    font-size: 9.5px;
    line-height: 12px;
    color: var(--grey-text);
  }
  .address-band {
    position: absolute;
    left: 34px;
    right: 33px;
    top: 252px;
    height: 22px;
    background: var(--navy);
    color: var(--paper);
    font-size: 13.5px;
    line-height: 22px;
    text-align: center;
  }
</style>
</head>
<body>
  <section class="card card--back" aria-label="Card back">
    <div class="texture" role="img" aria-label="Subtle tonal navy texture of overlapping squares"></div>
    <div class="brand">
      <span class="brand__square"></span>
      <span class="brand__name">ironquill build</span>
    </div>
  </section>

  <section class="card card--front" aria-label="Card front">
    <div class="brand">
      <span class="brand__square"></span>
      <span class="brand__name">ironquill build</span>
    </div>

    <div class="person">
      <p class="person__name">Daniel Harcourt</p>
      <p class="person__title">MANAGING DIRECTOR</p>
    </div>

    <ul class="contacts">
      <li><span class="contacts__label">p</span>1300 587 902</li>
      <li><span class="contacts__label">m</span>0438 761 205</li>
      <li><span class="contacts__label">e</span>d.harcourt@ironquillbuild.com.au</li>
      <li><span class="contacts__label">w</span>www.ironquillbuild.com.au</li>
    </ul>

    <div class="registration">
      <p>National Provider Number 7192</p>
      <p>ABN 53 614 289 117</p>
    </div>

    <p class="address-band">Level 1, 214 Garrow Street, Kelbridge NSW 2291</p>
  </section>
</body>
</html>
```